" Estamos a vinte anos no mercado, porem somos de porte pequeno em relação ao mercado. Fazemos abertura/encerramento de empresas, parte contábil, fiscal e departamento pessoal. Além de assessorar o cliente em duvidas corriqueiras que venham a sugir. "

```html
<!DOCTYPE html>
<html lang="pt-BR">
<head>
<meta charset="UTF-8">
<title>Vianna Assessoria Contábil — Papel Timbrado</title>
<link rel="stylesheet" href="https://fonts.googleapis.com/css2?family=Cinzel:wght@500&family=Open+Sans:wght@400&display=swap">
<style>
  :root {
    --backdrop: #e9e6e1;
    --paper: #ffffff;
    --navy: #1f3550;
    --navy-light: #3b5673;
    --ink-soft: #5b6470;
    --mark-tone: rgba(200, 202, 206, 0.28);
  }
  html, body {
    margin: 0;
    padding: 0;
    width: 1200px;
    height: 1200px;
    overflow: hidden;
    background: var(--backdrop);
  }
  .letterhead {
    position: absolute;
    left: 246px;
    top: 100px;
    width: 707px;
    height: 1000px;
    background: var(--paper);
    box-shadow: 0 6px 18px rgba(0,0,0,0.18);
    overflow: hidden;
  }
  .brand {
    position: absolute;
    left: 28px;
    top: 44px;
    display: flex;
    align-items: center;
    gap: 10px;
  }
  .brand-dot {
    width: 26px;
    height: 26px;
    border-radius: 50%;
    background: var(--navy);
  }
  .brand-text {
    display: flex;
    flex-direction: column;
    line-height: 1;
  }
  .brand-name {
    font-family: "Cinzel", serif;
    font-weight: 500;
    font-size: 40px;
    color: var(--navy);
    letter-spacing: 1px;
  }
  .brand-tagline {
    font-family: "Cinzel", serif;
    font-weight: 500;
    font-size: 9px;
    color: var(--navy);
    letter-spacing: 1.5px;
    margin-top: 4px;
    text-transform: uppercase;
  }
  .background-mark {
    position: absolute;
    left: 90px;
    top: 330px;
    width: 480px;
    height: 420px;
    background: radial-gradient(ellipse at center, var(--mark-tone) 0%, rgba(200,202,206,0.12) 45%, rgba(255,255,255,0) 72%);
  }
  .contact-line {
    position: absolute;
    left: 28px;
    right: 28px;
    top: 936px;
    margin: 0;
    font-family: "Open Sans", sans-serif;
    font-size: 12.5px;
    color: var(--ink-soft);
    white-space: nowrap;
    text-align: left;
  }
  .footer-band {
    position: absolute;
    left: 0;
    bottom: 0;
    width: 100%;
    height: 24px;
    background: var(--navy);
    border-top: 5px solid var(--navy-light);
  }
</style>
</head>
<body>
  <main class="letterhead">
    <header class="brand">
      <span class="brand-dot"></span>
      <div class="brand-text">
        <span class="brand-name">Vianna</span>
        <span class="brand-tagline">Assessoria Contábil</span>
      </div>
    </header>

    <div class="background-mark" role="img" aria-label="Marca d'água suave da empresa ao fundo da folha"></div>

    <p class="contact-line">(11) 4020-3150 | contato@viannacontabil.com.br | rua das acácias, 210 centro, são paulo</p>

    <footer class="footer-band"></footer>
  </main>
</body>
</html>
```